New Business Card

We need to refresh our business cards. We designed these ourselves and we have no graphic design experience. We would like to find a new business card design that is professional and unique. We are an auto finance company. Feel free to play with the logo, but we would like to keep the eye very present on the card. Our corporate colors are green, grey, and white.
Green - RGB - 168,215,27; HEX - #AADD22
Grey - RGB - 196,196,196; HEX - #C4C4C4
Updates
Need to upload the vector file to finalize the project. The last logo was for a jpeg that didn't stretch well.
Industry/Entity Type
Financial Service
Contact Information for Business Card
Honestly don't know...I need your help!

```html
<!DOCTYPE html>
<html lang="en">
<head>
<meta charset="utf-8">
<title>Brightlane Capital – Business Card</title>
<link href="https://fonts.googleapis.com/css2?family=Fira+Sans:wght@400;600&display=swap" rel="stylesheet">
<style>
  :root {
    --backdrop: #1d1e20;
    --card: #3a3b3e;
    --green: #aadd22;
    --grey: #c4c4c4;
    --white: #f2f2f2;
    --rule: #8a8b8e;
  }
  * { box-sizing: border-box; margin: 0; padding: 0; }
  html, body {
    width: 1200px; height: 676px; overflow: hidden;
    background: var(--backdrop);
    font-family: "Fira Sans", Arial, sans-serif;
  }
  .stage {
    position: relative; width: 1200px; height: 676px;
    display: flex; align-items: center; justify-content: center; gap: 60px;
  }
  .card {
    position: relative; width: 500px; height: 286px;
    background: var(--card); border-radius: 18px;
    box-shadow: 0 14px 30px rgba(0,0,0,.55);
  }
  .brand {
    display: flex; align-items: center; gap: 12px;
    font-weight: 600; color: var(--green); font-size: 34px; letter-spacing: .2px;
  }
  .brand-dot { width: 22px; height: 22px; border-radius: 50%; background: var(--green); }

  /* Front */
  .card--front .brand { position: absolute; top: 100px; left: 0; right: 0; justify-content: center; }
  .card--front .site {
    position: absolute; bottom: 48px; left: 0; right: 0; text-align: center;
    font-size: 13px; font-weight: 600; color: var(--white); letter-spacing: .4px;
  }
  .site .accent { color: var(--green); }

  /* Back */
  .card--back .brand { position: absolute; top: 56px; left: 0; right: 0; justify-content: center; font-size: 30px; }
  .details {
    position: absolute; left: 0; right: 0; top: 160px;
    display: flex; justify-content: center; align-items: stretch;
  }
  .person { text-align: right; padding-right: 18px; color: var(--white); font-size: 11.5px; line-height: 1.45; }
  .person-name { color: var(--green); font-weight: 600; font-size: 17px; letter-spacing: .5px; line-height: 1.2; margin-bottom: 2px; }
  .divider { width: 1px; background: var(--rule); }
  .contacts { list-style: none; padding-left: 16px; color: var(--white); font-size: 11.5px; line-height: 1.75; }
  .contacts li { display: flex; align-items: center; gap: 8px; }
  .contacts svg { width: 11px; height: 11px; fill: var(--green); flex: none; }
</style>
</head>
<body>
<main class="stage">
  <section class="card card--front">
    <div class="brand"><span class="brand-dot"></span>Brightlane Capital</div>
    <p class="site">www.<span class="accent">brightlanecapital</span>.com</p>
  </section>

  <section class="card card--back">
    <div class="brand"><span class="brand-dot"></span>Brightlane Capital</div>
    <div class="details">
      <div class="person">
        <p class="person-name">DANIEL R. HAYES</p>
        <p>Resident Manager</p>
        <p>Street Name Avenue, Suite</p>
        <p>100 State, Zip Code,Country</p>
      </div>
      <div class="divider"></div>
      <ul class="contacts">
        <li><svg viewBox="0 0 12 12"><path d="M2.5 0.5 L4.5 2.8 L3.5 4.2 Q4.7 6.8 7.8 8.5 L9.2 7.5 L11.5 9.5 L10 11.5 Q2 10 0.5 2 Z"/></svg>555-014-2270</li>
        <li><svg viewBox="0 0 12 12"><rect x="3" y="0.5" width="6" height="3"/><rect x="0.5" y="4" width="11" height="5" rx="1"/><rect x="3" y="8" width="6" height="3.5"/></svg>555-014-3381</li>
        <li><svg viewBox="0 0 12 12"><path d="M0.5 2 H11.5 V10 H0.5 Z M1.2 2.6 L6 6.5 L10.8 2.6 V3.6 L6 7.6 L1.2 3.6 Z" fill-rule="evenodd"/></svg>info@brightlanecapital.com</li>
        <li><svg viewBox="0 0 12 12"><path d="M6 0.5 A5.5 5.5 0 1 0 6 11.5 A5.5 5.5 0 1 0 6 0.5 Z M6 1.6 A4.4 4.4 0 1 1 6 10.4 A4.4 4.4 0 1 1 6 1.6 Z M5.5 1.6 H6.5 V10.4 H5.5 Z M1.6 5.5 H10.4 V6.5 H1.6 Z" fill-rule="evenodd"/></svg>www.brightlanecapital.com</li>
      </ul>
    </div>
  </section>
</main>
</body>
</html>
```